Construction training company needs a workshop invitation template

We need an invitation template for our professional development workshops we run for construction companies.
We would like to see designs that use the colors in our Framehold Sentinel Logo.
A simple, clean design with a lot of white space would be preferred.
No reverse text or italics.
The template should be done in Adobe Illustrator.

• Reverse text or italics

```html
<!DOCTYPE html>
<html lang="en">
<head>
<meta charset="utf-8">
<title>Framehold Sentinel – Workshop Invitation</title>
<link rel="stylesheet" href="https://fonts.googleapis.com/css2?family=Roboto+Condensed:wght@400;700&family=Roboto:wght@400;700&family=PT+Serif:wght@700&family=Montserrat:wght@700;800&display=swap">
<style>
  :root {
    --stage: #262626;
    --paper: #ffffff;
    --brown: #5b4a40;
    --green-dark: #1f6b3a;
    --green: #2e7a34;
    --green-light: #6aa52c;
    --olive: #6b8a1f;
    --accent-text: #5c8b16;
    --soft-grey: #eeeeee;
  }
  * { margin: 0; padding: 0; box-sizing: border-box; }
  html, body { width: 1200px; height: 1200px; overflow: hidden; background: var(--stage); }
  .card {
    position: absolute; left: 227px; width: 745px; height: 525px;
    background: var(--paper); overflow: hidden;
  }
  .card-front { top: 41px; }
  .card-back { top: 620px; }
  .texture {
    position: absolute; inset: 0;
    background: linear-gradient(160deg, rgba(255,255,255,0) 40%, var(--soft-grey) 100%);
  }
  .brand {
    position: absolute; display: flex; align-items: center; gap: 10px;
    font-family: "Montserrat", sans-serif; font-weight: 800; color: var(--brown);
    letter-spacing: 1.5px; text-transform: uppercase;
  }
  .brand-mark { background: var(--green); display: block; flex: none; }
  .brand-front { top: 44px; left: 0; right: 0; justify-content: center; font-size: 21px; }
  .brand-front .brand-mark { width: 40px; height: 40px; }

  .headline {
    position: absolute; top: 112px; left: 0; right: 0; text-align: center;
    font-family: "Roboto Condensed", sans-serif; font-weight: 400;
    font-size: 108px; line-height: 1; color: var(--brown); letter-spacing: -1px;
  }
  .invite-band {
    position: absolute; top: 226px; left: 0; width: 100%; height: 74px;
    background: linear-gradient(to bottom, var(--green-dark), var(--green-light));
    color: #fff; text-align: center;
    font-family: "Roboto Condensed", sans-serif; font-weight: 700; font-size: 24px; line-height: 29px;
    padding-top: 8px;
  }
  .event-date {
    position: absolute; top: 308px; left: 0; right: 0;
    display: flex; align-items: center; justify-content: center; gap: 14px;
    font-family: "Roboto Condensed", sans-serif; font-size: 31px; color: var(--green-dark);
  }
  .event-date .rule { width: 118px; height: 1px; background: var(--green-dark); }
  .event-meta {
    position: absolute; top: 353px; left: 0; right: 0;
    display: flex; justify-content: center; align-items: center; gap: 8px;
    font-family: "Roboto Condensed", sans-serif; font-size: 21px; color: #3c332d;
  }
  .event-meta svg { display: block; }
  .event-meta .gap { width: 10px; }
  .case-study {
    position: absolute; top: 388px; left: 0; right: 0; text-align: center;
    font-family: "Roboto", sans-serif; font-weight: 700; font-size: 13px; color: var(--accent-text);
  }
  .perks {
    position: absolute; top: 415px; left: 48px; width: 626px; height: 54px;
    display: flex; border: 1px solid var(--green);
    font-family: "Roboto", sans-serif; font-size: 13px; line-height: 18px;
  }
  .perks-food { flex: 1; padding: 8px 0 0 16px; color: #222; background: #fff; white-space: nowrap; }
  .perks-free { width: 185px; flex: none; background: var(--olive); color: #fff; padding: 8px 0 0 20px; font-size: 14.5px; white-space: nowrap; }
  .reverse-note {
    position: absolute; top: 488px; left: 0; right: 0;
    display: flex; justify-content: center; align-items: center; gap: 12px;
    font-family: "Roboto", sans-serif; font-weight: 700; font-size: 16px; color: var(--green);
  }
  .dot { width: 10px; height: 10px; border-radius: 50%; background: var(--green-light); }

  .back-heading {
    position: absolute; top: 20px; left: 105px;
    font-family: "PT Serif", serif; font-weight: 700; font-size: 27px; line-height: 36px;
    color: var(--green-dark); white-space: nowrap;
  }
  .back-heading .hl { color: var(--olive); }
  .heading-rule { position: absolute; top: 28px; left: 83px; width: 2px; height: 60px; background: var(--green); }
  .heading-rule::after {
    content: ""; position: absolute; top: 24px; left: -4px; width: 10px; height: 10px;
    border-radius: 50%; background: var(--green-light);
  }
  .topics {
    position: absolute; top: 100px; left: 86px; list-style: none;
    font-family: "PT Serif", serif; font-weight: 700; font-size: 14.2px; line-height: 18.9px; color: var(--brown);
  }
  .topics li { position: relative; padding-left: 19px; white-space: nowrap; }
  .topics svg { position: absolute; left: 0; top: 4px; }
  .cta-ribbon { position: absolute; top: 400px; left: 28px; width: 690px; height: 55px; }
  .cta-text {
    position: absolute; top: 409px; left: 81px; width: 586px; text-align: center;
    font-family: "Roboto", sans-serif; font-weight: 700; font-size: 22px; color: #fff;
  }
  .footer {
    position: absolute; top: 462px; left: 96px; height: 44px;
    display: flex; align-items: center;
  }
  .brand-back { position: static; font-size: 13px; gap: 8px; width: 180px; }
  .brand-back .brand-mark { width: 22px; height: 22px; }
  .footer .divider { width: 1px; height: 42px; background: var(--brown); margin: 0 12px 0 6px; }
  .contact {
    display: flex; align-items: center; gap: 8px;
    font-family: "Montserrat", sans-serif; font-weight: 700; font-size: 25px; color: var(--brown);
    white-space: nowrap;
  }
</style>
</head>
<body>

<section class="card card-front">
  <div class="texture" role="img" aria-label="Faint grey geometric tile pattern"></div>
  <div class="brand brand-front"><span class="brand-mark"></span>Framehold Sentinel</div>
  <h1 class="headline">You’re invited!</h1>
  <div class="invite-band">Brackwell Constructions invite you to a<br>Framehold Sentinel Professional Development Workshop</div>
  <div class="event-date"><span class="rule"></span>Wednesday the 7th of June 2021<span class="rule"></span></div>
  <div class="event-meta">
    <svg width="14" height="18" viewBox="0 0 14 18"><path d="M7 0C3.1 0 0 3.1 0 7c0 5 7 11 7 11s7-6 7-11c0-3.9-3.1-7-7-7z" fill="var(--green)"/><circle cx="7" cy="7" r="2.6" fill="#fff"/></svg>
    <span>At [address of venue inserted here]</span>
    <span class="gap"></span>
    <svg width="15" height="18" viewBox="0 0 15 18"><path d="M1 1h13M1 17h13M3 1c0 5 9 5 9 8s-9 3-9 8M12 1c0 5-9 5-9 8s9 3 9 8" fill="none" stroke="var(--green)" stroke-width="2"/></svg>
    <span>7:00 AM to 12 noon</span>
  </div>
  <p class="case-study">The case study at this workshop will be the Brackwell Constructions project at 14 Tallow St, Ridgeway</p>
  <div class="perks">
    <p class="perks-food">Enjoy some good coffee at the start and awesome food<br>or lunch at the end —all compliments of Brackwell Constructions</p>
    <p class="perks-free">And there's no charge<br>for attending!</p>
  </div>
  <div class="reverse-note"><span class="dot"></span>See Reverse side for more info...<span class="dot"></span></div>
</section>

<section class="card card-back">
  <div class="texture" role="img" aria-label="Faint grey geometric tile pattern"></div>
  <span class="heading-rule"></span>
  <h2 class="back-heading">This is a <span class="hl">live action</span> workshop<br>where&nbsp; you <span class="hl">participate in and learn about..</span></h2>
  <ul class="topics">
    <li><svg width="11" height="10" viewBox="0 0 11 10"><rect x="0.7" y="1.7" width="7.6" height="7.6" fill="none" stroke="var(--green)" stroke-width="1.4"/><path d="M2.5 5l2 2L10 1" fill="none" stroke="var(--green)" stroke-width="1.8"/></svg>How to set up a smart schedule for a construction project</li>
    <li><svg width="11" height="10" viewBox="0 0 11 10"><rect x="0.7" y="1.7" width="7.6" height="7.6" fill="none" stroke="var(--green)" stroke-width="1.4"/><path d="M2.5 5l2 2L10 1" fill="none" stroke="var(--green)" stroke-width="1.8"/></svg>How to get clarity on the building work to be done, using a 3D model (etc)</li>
    <li><svg width="11" height="10" viewBox="0 0 11 10"><rect x="0.7" y="1.7" width="7.6" height="7.6" fill="none" stroke="var(--green)" stroke-width="1.4"/><path d="M2.5 5l2 2L10 1" fill="none" stroke="var(--green)" stroke-width="1.8"/></svg>Getting everybody on the same page</li>
    <li><svg width="11" height="10" viewBox="0 0 11 10"><rect x="0.7" y="1.7" width="7.6" height="7.6" fill="none" stroke="var(--green)" stroke-width="1.4"/><path d="M2.5 5l2 2L10 1" fill="none" stroke="var(--green)" stroke-width="1.8"/></svg>Solving construction headaches before they happen</li>
    <li><svg width="11" height="10" viewBox="0 0 11 10"><rect x="0.7" y="1.7" width="7.6" height="7.6" fill="none" stroke="var(--green)" stroke-width="1.4"/><path d="M2.5 5l2 2L10 1" fill="none" stroke="var(--green)" stroke-width="1.8"/></svg>Getting the information you need to make you more efficient and effective</li>
    <li><svg width="11" height="10" viewBox="0 0 11 10"><rect x="0.7" y="1.7" width="7.6" height="7.6" fill="none" stroke="var(--green)" stroke-width="1.4"/><path d="M2.5 5l2 2L10 1" fill="none" stroke="var(--green)" stroke-width="1.8"/></svg>How to get more satisfaction out of your work</li>
    <li><svg width="11" height="10" viewBox="0 0 11 10"><rect x="0.7" y="1.7" width="7.6" height="7.6" fill="none" stroke="var(--green)" stroke-width="1.4"/><path d="M2.5 5l2 2L10 1" fill="none" stroke="var(--green)" stroke-width="1.8"/></svg>Delivering projects in less time and at lower costs</li>
    <li><svg width="11" height="10" viewBox="0 0 11 10"><rect x="0.7" y="1.7" width="7.6" height="7.6" fill="none" stroke="var(--green)" stroke-width="1.4"/><path d="M2.5 5l2 2L10 1" fill="none" stroke="var(--green)" stroke-width="1.8"/></svg>Achieving better quality work and Ensuring a high level of worksite safety</li>
    <li><svg width="11" height="10" viewBox="0 0 11 10"><rect x="0.7" y="1.7" width="7.6" height="7.6" fill="none" stroke="var(--green)" stroke-width="1.4"/><path d="M2.5 5l2 2L10 1" fill="none" stroke="var(--green)" stroke-width="1.8"/></svg>Developing stronger relationships within the workforce</li>
    <li><svg width="11" height="10" viewBox="0 0 11 10"><rect x="0.7" y="1.7" width="7.6" height="7.6" fill="none" stroke="var(--green)" stroke-width="1.4"/><path d="M2.5 5l2 2L10 1" fill="none" stroke="var(--green)" stroke-width="1.8"/></svg>How smart collaboration can improve things for everybody</li>
    <li><svg width="11" height="10" viewBox="0 0 11 10"><rect x="0.7" y="1.7" width="7.6" height="7.6" fill="none" stroke="var(--green)" stroke-width="1.4"/><path d="M2.5 5l2 2L10 1" fill="none" stroke="var(--green)" stroke-width="1.8"/></svg>Transforming workplace culture and reducing the mental health issue<br>in the construction industry</li>
    <li><svg width="11" height="10" viewBox="0 0 11 10"><rect x="0.7" y="1.7" width="7.6" height="7.6" fill="none" stroke="var(--green)" stroke-width="1.4"/><path d="M2.5 5l2 2L10 1" fill="none" stroke="var(--green)" stroke-width="1.8"/></svg>Reducing rework and warranty work</li>
    <li><svg width="11" height="10" viewBox="0 0 11 10"><rect x="0.7" y="1.7" width="7.6" height="7.6" fill="none" stroke="var(--green)" stroke-width="1.4"/><path d="M2.5 5l2 2L10 1" fill="none" stroke="var(--green)" stroke-width="1.8"/></svg>Creating better results, with less time, effort and cost</li>
    <li><svg width="11" height="10" viewBox="0 0 11 10"><rect x="0.7" y="1.7" width="7.6" height="7.6" fill="none" stroke="var(--green)" stroke-width="1.4"/><path d="M2.5 5l2 2L10 1" fill="none" stroke="var(--green)" stroke-width="1.8"/></svg>Boosting customer satisfaction and referrals</li>
  </ul>

  <svg class="cta-ribbon" viewBox="0 0 690 55">
    <defs>
      <linearGradient id="ribbon-fill" x1="0" y1="0" x2="0" y2="1">
        <stop offset="0" stop-color="#1f6b3a"/><stop offset="1" stop-color="#6aa52c"/>
      </linearGradient>
    </defs>
    <polygon points="0,10 50,10 50,52 0,52 18,31" fill="#3f8a2e"/>
    <polygon points="690,10 640,10 640,52 690,52 672,31" fill="#3f8a2e"/>
    <polygon points="50,44 70,52 50,52" fill="#1a5a2e"/>
    <polygon points="640,44 620,52 640,52" fill="#1a5a2e"/>
    <rect x="53" y="0" width="586" height="44" fill="url(#ribbon-fill)"/>
  </svg>
  <p class="cta-text">Seats are limited, so book your spot today!</p>

  <div class="footer">
    <div class="brand brand-back"><span class="brand-mark"></span>Framehold Sentinel</div>
    <span class="divider"></span>
    <div class="contact">
      <svg width="24" height="24" viewBox="0 0 24 24"><path d="M6.6 10.8a15 15 0 0 0 6.6 6.6l2.2-2.2a1 1 0 0 1 1-.25 11.4 11.4 0 0 0 3.6.6 1 1 0 0 1 1 1V20a1 1 0 0 1-1 1A17 17 0 0 1 3 4a1 1 0 0 1 1-1h3.5a1 1 0 0 1 1 1c0 1.25.2 2.45.6 3.6a1 1 0 0 1-.25 1z" fill="var(--brown)"/></svg>
      <span>Dana on 0400 000 000</span>
    </div>
  </div>
</section>

</body>
</html>
```